Business card design needed

It's a new business in town.Something so the name stands out.I need a logo for the B.R.W
I may all so use the design as a sign on a building

Contact Information for Business Card

B.R.W
Brindlewood Auto Detailing
42 Fenwarra Crs
Brindlewood Vic 3799
Ph:(03)59284736
Mob:0417362958

```html
<!DOCTYPE html>
<html lang="en">
<head>
<meta charset="utf-8">
<title>B.R.W – Brindlewood Auto Detailing business card</title>
<link rel="stylesheet" href="https://fonts.googleapis.com/css2?family=Open+Sans:wght@400;700&display=swap">
<style>
  :root {
    --page-bg: #e9e7e4;
    --card-base: #262626;
    --card-light: #4a4a4a;
    --ink-light: #ffffff;
    --ink-dark: #111111;
    --panel: #ffffff;
  }
  * { margin: 0; padding: 0; box-sizing: border-box; }
  html, body {
    width: 1200px;
    height: 1000px;
    overflow: hidden;
    background: var(--page-bg);
  }
  .canvas {
    position: relative;
    width: 1200px;
    height: 1000px;
  }
  .business-card {
    position: absolute;
    left: 100px;
    top: 215px;
    width: 1000px;
    height: 570px;
    overflow: hidden;
    background:
      radial-gradient(circle 380px at 610px 215px, var(--card-light) 0%, #3a3a3a 55%, var(--card-base) 100%),
      var(--card-base);
    box-shadow: 0 10px 30px rgba(0,0,0,0.25);
  }
  .brand {
    position: absolute;
    left: 420px;
    top: 95px;
    width: 520px;
    text-align: center;
    color: var(--ink-light);
    font-family: "Open Sans", sans-serif;
  }
  .brand-emblem {
    display: block;
    width: 490px;
    height: 120px;
    margin: 0 auto 6px;
  }
  .brand-name {
    font-size: 104px;
    font-weight: 400;
    line-height: 1;
    letter-spacing: 6px;
  }
  .brand-tagline {
    margin-top: 6px;
    font-size: 29px;
    font-weight: 400;
    letter-spacing: 0.3px;
  }
  .contact-panel {
    position: absolute;
    left: 0;
    top: 347px;
    width: 342px;
    height: 141px;
    background: var(--panel);
    padding: 14px 0 0 26px;
    font-family: "Open Sans", sans-serif;
    font-weight: 700;
    font-size: 19px;
    line-height: 31px;
    color: var(--ink-dark);
    list-style: none;
  }
</style>
</head>
<body>
<main class="canvas">
  <section class="business-card" aria-label="Business card">
    <div class="brand">
      <svg class="brand-emblem" role="img" aria-label="Line drawing of a sports car in profile" viewBox="0 0 490 120">
        <rect x="0" y="0" width="490" height="120" rx="10" fill="#5a5a5a" opacity="0.45"/>
      </svg>
      <div class="brand-name">B.R.W</div>
      <div class="brand-tagline">Brindlewood Auto Detailing</div>
    </div>
    <ul class="contact-panel">
      <li>42 Fenwarra Crs</li>
      <li>Brindlewood Vic 3799 Ph</li>
      <li>Tel : (03)59284736</li>
      <li>Mob : 0417362958</li>
    </ul>
  </section>
</main>
</body>
</html>
```